Business Card Design for Occupational Medicine Start Up Company

We need to design a professional business card. We are a healthcare company providing occupational medicine services to blue collar industries. We are professional, efficient and high quality service providers.

Target Market(s)

Blue Collar Industry: Shipbuilding, Ports, Trucking Companies; The Executives and Safety Officers for these companies

Industry/Entity Type

Healthcare

Contact Information for Business Card

Logo, Name, Title, Email, Phone

Other font styles liked:
• Please match our Brand Guide

Requirements
Must have
• Our Company Colors and Logo

```html
<!DOCTYPE html>
<html lang="en">
<head>
<meta charset="utf-8">
<title>Harborline Clinics – Business Card</title>
<link rel="stylesheet" href="https://fonts.googleapis.com/css2?family=Montserrat:wght@400;500;600&display=swap">
<style>
  :root {
    --page-bg: #d9d6d2;
    --card-bg: #eef0f1;
    --card-bg-edge: #dfe3e5;
    --navy: #363a8c;
    --navy-deep: #2b2f7a;
    --amber: #e6a43a;
    --teal: #2b8ea4;
    --ink: #3a3d4a;
    --ink-soft: #4b4e5c;
    --brand-text: #e9e4dc;
  }
  * { margin: 0; padding: 0; box-sizing: border-box; }
  html, body {
    width: 1200px;
    height: 1054px;
    overflow: hidden;
    background: var(--page-bg);
    font-family: "Montserrat", Arial, sans-serif;
  }
  .business-card {
    position: absolute;
    left: 120px;
    top: 238px;
    width: 960px;
    height: 578px;
    border-radius: 22px;
    overflow: hidden;
    background: linear-gradient(160deg, var(--card-bg) 0%, var(--card-bg-edge) 100%);
    box-shadow: 0 10px 30px rgba(0, 0, 0, 0.18);
  }
  .brand-panel {
    position: absolute;
    inset: 0;
    width: 100%;
    height: 100%;
  }
  .brand-block {
    position: absolute;
    left: 0;
    top: 150px;
    width: 440px;
    text-align: center;
    color: var(--brand-text);
  }
  .brand-mark {
    width: 64px;
    height: 64px;
    margin: 0 auto 34px;
    border-radius: 50%;
    background: var(--amber);
  }
  .brand-name {
    font-size: 34px;
    font-weight: 600;
    letter-spacing: 1px;
    line-height: 1.25;
    text-transform: uppercase;
  }
  .contact-side {
    position: absolute;
    left: 535px;
    top: 0;
    right: 0;
    bottom: 0;
    color: var(--ink);
  }
  .person-name {
    position: absolute;
    top: 136px;
    font-size: 38px;
    font-weight: 500;
    letter-spacing: 1px;
    color: var(--teal);
    text-transform: uppercase;
  }
  .person-title {
    position: absolute;
    top: 184px;
    font-size: 23px;
    font-weight: 400;
    color: var(--ink-soft);
  }
  .contact-row {
    position: absolute;
    left: 0;
    display: flex;
    align-items: flex-start;
    font-size: 23px;
    font-weight: 400;
    line-height: 36px;
  }
  .contact-row .icon {
    width: 24px;
    height: 24px;
    margin: 6px 19px 0 0;
    flex: none;
  }
  .row-phone { top: 246px; }
  .row-email { top: 281px; }
  .row-web { top: 316px; }
  .row-address { top: 357px; }
</style>
</head>
<body>
  <div class="business-card">
    <svg class="brand-panel" viewBox="0 0 960 578" preserveAspectRatio="none" aria-hidden="true">
      <path d="M0 0 H410 C520 110 530 420 385 578 H0 Z" fill="var(--amber)"/>
      <path d="M0 0 H398 C505 115 512 420 372 578 H0 Z" fill="var(--navy)"/>
      <path d="M0 0 H398 C505 115 512 420 372 578 H0 Z" fill="url(#panelShade)"/>
      <defs>
        <linearGradient id="panelShade" x1="0" y1="0" x2="1" y2="1">
          <stop offset="0" stop-color="var(--navy)" stop-opacity="0"/>
          <stop offset="1" stop-color="var(--navy-deep)" stop-opacity="0.6"/>
        </linearGradient>
      </defs>
    </svg>

    <div class="brand-block">
      <div class="brand-mark"></div>
      <div class="brand-name">Harborline<br>Clinics</div>
    </div>

    <div class="contact-side">
      <div class="person-name">Dana Reyes</div>
      <div class="person-title">Senior Doctor</div>

      <div class="contact-row row-phone">
        <svg class="icon" viewBox="0 0 24 24" aria-hidden="true">
          <path d="M3 9 C3 5 21 5 21 9 L18 11 L16 8.5 H8 L6 11 Z" fill="var(--teal)"/>
          <rect x="5" y="12" width="14" height="8" rx="2" fill="var(--teal)"/>
        </svg>
        <span>555-014-2290</span>
      </div>

      <div class="contact-row row-email">
        <svg class="icon" viewBox="0 0 24 24" aria-hidden="true">
          <rect x="3" y="6" width="18" height="13" rx="1" fill="var(--navy)"/>
          <path d="M3.5 6.5 L12 13 L20.5 6.5" stroke="#fff" stroke-width="1.5" fill="none"/>
        </svg>
        <span>dana@harborline.com</span>
      </div>

      <div class="contact-row row-web">
        <svg class="icon" viewBox="0 0 24 24" aria-hidden="true">
          <circle cx="12" cy="12" r="8" fill="var(--amber)"/>
          <path d="M4 12 H20 M12 4 C8 8 8 16 12 20 M12 4 C16 8 16 16 12 20" stroke="#fff" stroke-width="1.2" fill="none"/>
        </svg>
        <span>www.harborline.com</span>
      </div>

      <div class="contact-row row-address">
        <svg class="icon" viewBox="0 0 24 24" aria-hidden="true">
          <path d="M12 2 C7.5 2 5 5.3 5 9 C5 14 12 22 12 22 C12 22 19 14 19 9 C19 5.3 16.5 2 12 2 Z" fill="var(--amber)"/>
          <circle cx="12" cy="9" r="2.8" fill="#fff"/>
        </svg>
        <span>48 Dockside Avenue, Suite 210<br>Portview, State 54321</span>
      </div>
    </div>
  </div>
</body>
</html>
```